We are Here! Come and Meet the Team Flyer

A clear and quirky, flyer to let local Residents know we have landed.
Based around our logo.

We avoid anything medical but rather focus on being pet-centred, warmth, approachable and community-orientated.

We pride ourselves on being cutting-edge but steer away from a cold sterile image.
Approachability, uptodate. We understandt hat pets are part of a family and we will provide the level of care that we would expect for our own pets.

Target Market(s)

Residents in the area

Industry/Entity Type

Veterinary

Font styles to use
Sans Serif

Colors
33b8a4
ffc214
0255a3

Requirements
Must have
• Logo and PERHAPS a location of Clinic indicated on the cat of the Logo.
• NOW OPEN!
• 1) Exact location of the Clinic indicated: the lefthand side of tail, near the cat's back.
• 2) Warm, quirky, Approachable
• 3) Contact details (see attached draft Poster)
• 4) Location: Silver Brook Arcade, Building 4, Mezzanine level
Should not have
• nothing medical or cliched.

```html
<!DOCTYPE html>
<html lang="en">
<head>
<meta charset="utf-8">
<title>Tails &amp; Toes Veterinary Clinic – Now Open</title>
<link href="https://fonts.googleapis.com/css2?family=Montserrat:ital,wght@0,400;0,500;0,600;0,700;0,800;1,300;1,700;1,800&display=swap" rel="stylesheet">
<style>
  :root{
    --blue:#0255a3;
    --teal:#33b8a4;
    --yellow:#ffc214;
    --ink:#222a30;
    --brand:#2b6f7e;
    --white:#ffffff;
    --stage:#e4e4e4;
  }
  *{margin:0;padding:0;box-sizing:border-box;}
  html,body{width:1197px;height:1200px;overflow:hidden;background:var(--stage);}
  body{font-family:'Montserrat',sans-serif;position:relative;}
  .flyer{position:absolute;left:160px;top:20px;width:877px;height:1159px;overflow:hidden;background:var(--white);}
  .flyer-bands{position:absolute;inset:0;}
  .header{position:absolute;left:0;top:0;width:877px;height:180px;}
  .brand{position:absolute;left:36px;top:62px;display:flex;align-items:center;gap:16px;}
  .brand-dot{width:52px;height:52px;border-radius:50%;background:var(--teal);}
  .brand-name{font-size:34px;font-weight:600;color:var(--brand);letter-spacing:.5px;}
  .location{position:absolute;left:360px;top:42px;display:flex;gap:12px;}
  .location-pin{width:24px;height:32px;margin-top:2px;flex:none;}
  .address{font-style:normal;font-size:18.5px;font-weight:700;color:var(--ink);line-height:27.5px;}
  .now-open{position:absolute;left:47px;top:198px;font-size:22px;font-weight:800;color:var(--yellow);letter-spacing:1.5px;}
  .headline{position:absolute;left:47px;top:232px;color:var(--white);}
  .headline .place{font-size:33px;font-weight:800;font-style:italic;line-height:44px;}
  .headline .own{font-size:30px;font-weight:300;font-style:italic;line-height:40px;}
  .headline .clinic{font-size:36px;font-weight:800;font-style:italic;line-height:46px;}
  .services{position:absolute;left:47px;top:385px;color:var(--white);}
  .services h2{font-size:16px;font-weight:700;margin-bottom:12px;}
  .services ul{list-style:none;}
  .services li{display:flex;align-items:center;height:34.2px;font-size:13.5px;font-weight:500;}
  .services svg{width:20px;height:20px;margin-right:25px;stroke:var(--white);fill:none;stroke-width:1.5;}
  .photo{position:absolute;border:3px solid var(--white);}
  .photo-main{left:355px;top:253px;width:514px;height:514px;border-radius:50% 50% 50% 0;
    background:linear-gradient(135deg,#e9e2d8 0%,#cdbfae 40%,#6f645c 70%,#3b3540 100%);}
  .photo-room{left:61px;top:729px;width:282px;height:282px;border-radius:50% 0 50% 50%;
    background:linear-gradient(90deg,#b3855a 0%,#c9a27b 45%,#3fbfc4 60%,#d7dee0 100%);}
  .photo-cat{left:355px;top:780px;width:151px;height:151px;border-radius:0 50% 50% 50%;
    background:linear-gradient(135deg,#e9e7e2 0%,#b49d7f 50%,#5b4a3a 100%);}
  .contact{position:absolute;right:63px;top:828px;text-align:right;color:var(--white);}
  .contact h2{font-size:25px;font-weight:800;margin-bottom:10px;letter-spacing:.3px;}
  .contact p{font-size:16px;font-weight:700;line-height:34px;letter-spacing:.4px;}
  .open{position:absolute;right:60px;top:1018px;font-size:44px;font-weight:800;font-style:italic;color:var(--white);letter-spacing:.5px;}
  .rule{position:absolute;left:150px;right:50px;top:1085px;height:1px;background:rgba(255,255,255,.35);}
  .social{position:absolute;top:1104px;display:flex;align-items:center;gap:9px;font-size:14.5px;font-weight:500;color:var(--ink);}
  .social i{display:block;width:24px;height:24px;background:var(--blue);border-radius:3px;}
  .social.s2 i{border-radius:50%;}
  .social.s3 i{background:var(--ink);}
</style>
</head>
<body>
<main class="flyer">
  <svg class="flyer-bands" width="877" height="1159" viewBox="0 0 877 1159" aria-hidden="true">
    <rect x="0" y="180" width="877" height="979" fill="var(--blue)"/>
    <polygon points="877,0 877,1159 0,1159" fill="var(--yellow)"/>
    <polygon points="877,177 877,1159 134,1159" fill="var(--teal)"/>
  </svg>

  <header class="header">
    <div class="brand">
      <span class="brand-dot"></span>
      <span class="brand-name">Tails &amp; Toes</span>
    </div>
    <div class="location">
      <svg class="location-pin" viewBox="0 0 24 32" aria-hidden="true">
        <path d="M12 1C6 1 1.5 5.5 1.5 11.5C1.5 19 12 31 12 31S22.5 19 22.5 11.5C22.5 5.5 18 1 12 1z" fill="var(--teal)"/>
        <circle cx="12" cy="11.5" r="4" fill="var(--white)"/>
      </svg>
      <address class="address">
        Building 4, Mezzanine Level,<br>
        Silver Brook Arcade,<br>
        Above Cafe Lumo<br>
        Marlow Bay, Coastline District
      </address>
    </div>
  </header>

  <div class="now-open">NOW OPEN!</div>

  <section class="headline">
    <div class="place">The ISLE HARBOUR</div>
    <div class="own">now has its own</div>
    <div class="clinic">Veterinary Clinic</div>
  </section>

  <section class="services">
    <h2>Come and Meet the Team:</h2>
    <ul>
      <li><svg viewBox="0 0 20 20"><path d="M10 17L3 10a4 4 0 0 1 7-5a4 4 0 0 1 7 5z"/></svg>Friendly Family Pet Care</li>
      <li><svg viewBox="0 0 20 20"><path d="M3 4h14v9H8l-4 3v-3H3z"/></svg>Pet Parent Chats &amp; Advice</li>
      <li><svg viewBox="0 0 20 20"><path d="M10 2l2.4 5 5.4.6-4 3.7 1.1 5.4L10 14l-4.9 2.7 1.1-5.4-4-3.7 5.4-.6z"/></svg>Puppy &amp; Kitten Welcome</li>
      <li><svg viewBox="0 0 20 20"><path d="M3 10l7-6 7 6M5 9v8h10V9"/></svg>A Home From Home</li>
      <li><svg viewBox="0 0 20 20"><path d="M2 15h16M3 15l2-6h10l2 6"/></svg>Diet &amp; Nutrition</li>
      <li><svg viewBox="0 0 20 20"><rect x="3" y="4" width="14" height="13"/><path d="M3 8h14M7 2v4M13 2v4"/></svg>Open Days &amp; Socials</li>
      <li><svg viewBox="0 0 20 20"><circle cx="7" cy="8" r="3"/><circle cx="14" cy="9" r="2.5"/><path d="M2 17c0-3 2.5-5 5-5s5 2 5 5M12 17c0-2 1-4 4-4"/></svg>Community Pet Events</li>
      <li><svg viewBox="0 0 20 20"><path d="M4 10l4 4 8-8"/></svg>Happy Pet Plans</li>
    </ul>
  </section>

  <div class="photo photo-main" role="img" aria-label="Photo of a young girl at the clinic counter with a fluffy white dog"></div>
  <div class="photo photo-room" role="img" aria-label="Photo of the clinic reception with shelves of pet food and a teal wall"></div>
  <div class="photo photo-cat" role="img" aria-label="Photo of a tabby cat resting in a clinic kennel"></div>

  <section class="contact">
    <h2>CONTACT US:</h2>
    <p>Call: 800-PAWS-VET</p>
    <p>Call: 04 555 0192</p>
    <p>www.tailsandtoes.example</p>
    <p>hello@tailsandtoes.example</p>
  </section>

  <div class="open">OPEN 7 DAYS A WEEK</div>
  <div class="rule"></div>

  <div class="social s1" style="left:167px"><i></i>@TTVetsHarbour</div>
  <div class="social s2" style="left:442px"><i></i>@tailstoesvet</div>
  <div class="social s3" style="left:671px"><i></i>@ttvetclinic</div>
</main>
</body>
</html>
```